Plinthmoor Assessments Landing Page

We need a landing page re-designed for a new website www.plinthmoorassessments.example and the website is live if you search the address provided.
We need the industry standard files for embedding this into the landing page of our website. The company is a real estate advisory firm, we provide professional property services and are focused on business rates (commercial property taxation in the UK).
We have uploaded a file which is meant to provide a visual guide as to how we envisage the landing page looking. You are free to come up with an entirely different creative design. The image at the top with the search button is taken from another website so the design will need to be distinctly different but may follow the same theme. Furthermore, the colour palette does not need to be followed slavishly and can be modified changed and improved upon. It might be that you want to incorporate other visual cues such as a desktop PC, laptop and iPad as these are devices the website will be accessed from; however, this is not essential and only a guide.
**To clarify, please note, the target industry is commercial properties and not residential or domestic property, so please when incorporating designs of buildings its important to focus on commercial property such as shops, offices, industrial buildings etc.**
Target Market(s)
Occupiers of commercial real estate in the UK who pay property tax to occupy the property.
Look and feel
Each slider illustrates characteristics of the customer's brand and the style your logo design should communicate.

```html
<!DOCTYPE html>
<html lang="en">
<head>
<meta charset="utf-8">
<title>Plinthmoor Assessments – Business Rates Valuations</title>
<link rel="stylesheet" href="https://fonts.googleapis.com/css2?family=Lato:ital,wght@0,400;0,700;0,900;1,400&family=Varela+Round&display=swap">
<style>
:root{
  --navy:#0b1f3e;
  --orange:#ff5a1f;
  --orange-deep:#dd5a06;
  --green:#00d184;
  --white:#ffffff;
  --ink:#2b2b2b;
  --grey-text:#6f6f6f;
  --grey-head:#8a8a8a;
  --soft-bg:#f5f5f5;
  --circle:#f3f3f3;
  --purple-a:#2a1b6b;
  --purple-b:#3b2a8e;
}
*{box-sizing:border-box;margin:0;padding:0}
html,body{width:1200px;height:2300px;overflow:hidden}
body{font-family:"Lato",sans-serif;color:var(--ink);background:var(--white);position:relative}
a{color:inherit;text-decoration:none}

.topbar{position:absolute;top:0;left:0;width:1200px;height:43px;background:var(--navy)}
.btn-small{position:absolute;top:7px;height:29px;background:var(--orange);color:var(--white);font-size:10px;font-weight:900;display:flex;align-items:center;justify-content:center;letter-spacing:.2px}
.btn-contact{left:88px;width:100px}
.btn-book-top{left:967px;width:152px}
.social-top{position:absolute;top:15px;left:214px;display:flex;gap:26px}
.dot{width:11px;height:11px;border-radius:50%;background:var(--orange)}
.account-link{position:absolute;top:14px;color:var(--white);font-size:12px;display:flex;align-items:center;gap:7px}
.account-link.my{left:738px}
.account-link.out{left:872px}

.mainnav{position:absolute;top:43px;left:0;width:1200px;height:58px;background:var(--white)}
.brand{position:absolute;left:86px;top:19px;display:flex;align-items:center;gap:7px;font-size:12px;font-weight:700;color:var(--ink);letter-spacing:.3px}
.brand-mark{width:16px;height:16px;background:var(--orange)}
.nav-link{position:absolute;top:22px;font-size:14px;letter-spacing:.6px;color:#333}
.badge{position:absolute;left:1028px;top:17px;width:60px;height:24px;border-radius:4px;background:#1c1c1c}

.hero{position:absolute;top:101px;left:0;width:1200px;height:588px;background:linear-gradient(180deg,#7d93a8 0%,#5e7890 40%,#3e5a74 70%,#2f4862 100%)}
.hero-title{position:absolute;top:210px;left:120px;width:960px;text-align:center;color:var(--white);font-size:36px;font-weight:900;letter-spacing:2px;line-height:54px}
.hero-sub{position:absolute;top:319px;left:120px;width:960px;text-align:center;color:var(--white);font-size:26px;font-style:italic;line-height:34px}
.search{position:absolute;top:455px;left:239px;width:720px;height:54px;background:var(--white);display:flex;align-items:center;justify-content:space-between;padding:0 5px 0 29px}
.search-hint{font-size:13px;color:#8d8d8d;letter-spacing:.4px}
.search-btn{width:176px;height:42px;background:var(--green);color:var(--white);font-size:12px;font-weight:900;letter-spacing:.6px;display:flex;align-items:center;justify-content:center}

.features-title{position:absolute;top:757px;left:0;width:1200px;text-align:center;font-size:27px;font-weight:700;color:var(--grey-head);letter-spacing:.5px}
.feature{position:absolute;top:839px;width:300px}
.feature-icon{width:144px;height:144px;border-radius:50%;background:var(--circle);display:flex;align-items:center;justify-content:center}
.feature-text{margin-top:12px;font-size:15px;line-height:26.7px;color:var(--grey-text);letter-spacing:.3px}

.covered{position:absolute;top:1225px;left:0;width:1200px;height:297px;background:linear-gradient(90deg,#20165a 0%,var(--purple-b) 45%,#2e2275 75%,#1d1552 100%)}
.covered-title{position:absolute;top:86px;left:113px;font-family:"Varela Round",sans-serif;font-size:36px;color:var(--white);letter-spacing:1px}
.covered-text{position:absolute;top:161px;left:114px;width:960px;font-family:"Varela Round",sans-serif;font-size:23px;line-height:40px;color:var(--white)}

.fees{position:absolute;top:1522px;left:0;width:1200px;height:386px;background:var(--soft-bg)}
.fees-title{position:absolute;top:70px;left:108px;font-family:"Varela Round",sans-serif;font-size:30px;color:#2d2d2d;letter-spacing:1px}
.fees-text{position:absolute;top:126px;left:110px;width:990px;font-size:19.5px;line-height:40px;color:var(--grey-text)}

.cta{position:absolute;top:1908px;left:0;width:1200px;height:128px;background:var(--navy)}
.cta-text{position:absolute;top:50px;left:86px;color:var(--white);font-size:20px;font-weight:700;letter-spacing:.6px}
.cta-btn{position:absolute;top:34px;left:838px;width:272px;height:59px;background:var(--orange-deep);color:var(--white);font-size:17px;display:flex;align-items:center;justify-content:center;letter-spacing:.3px}

.footer-nav{position:absolute;top:2036px;left:0;width:1200px;height:94px;border-bottom:1px solid #dedede}
.footer-link{position:absolute;top:40px;font-size:15px;letter-spacing:.5px;color:#333}
.company-info{position:absolute;left:82px;font-size:13px;letter-spacing:.4px;color:#333}
.company-info b{font-weight:700}
.follow{position:absolute;top:2165px;left:881px;font-size:13px;display:flex;align-items:center;gap:14px;color:#333}
.dot-blue{width:10px;height:10px;border-radius:50%;background:#1a7fc9}
.copyright{position:absolute;top:2243px;left:78px;font-size:12px;color:#333}
</style>
</head>
<body>

<header class="topbar">
  <a class="btn-small btn-contact" href="#">CONTACT US</a>
  <div class="social-top" aria-label="Social links">
    <span class="dot"></span><span class="dot"></span><span class="dot"></span>
  </div>
  <a class="account-link my" href="#">
    <svg width="10" height="11" viewBox="0 0 10 11"><circle cx="5" cy="3" r="2.6" fill="var(--orange)"/><path d="M0 11c0-3 2-4.5 5-4.5s5 1.5 5 4.5z" fill="var(--orange)"/></svg>
    My Account
  </a>
  <a class="account-link out" href="#">
    <svg width="12" height="12" viewBox="0 0 12 12"><path d="M3.5 2.8A4.6 4.6 0 1 0 8.5 2.8" fill="none" stroke="var(--orange)" stroke-width="1.5" stroke-linecap="round"/><line x1="6" y1="0.8" x2="6" y2="5.5" stroke="var(--orange)" stroke-width="1.5" stroke-linecap="round"/></svg>
    Log out
  </a>
  <a class="btn-small btn-book-top" href="#">BOOK VALUATION NOW</a>
</header>

<nav class="mainnav">
  <div class="brand"><span class="brand-mark"></span>PLINTHMOOR ASSESSMENTS</div>
  <a class="nav-link" style="left:625px" href="#">PROPERTY SEARCH</a>
  <a class="nav-link" style="left:814px" href="#">DISCOVER</a>
  <a class="nav-link" style="left:940px" href="#">ABOUT</a>
  <span class="badge" aria-label="Professional accreditation badge"></span>
</nav>

<section class="hero" role="img" aria-label="Blurred city skyline of commercial office towers seen over a tablet held in hand">
  <h1 class="hero-title">DO YOU THINK YOUR BUSINESS RATES ARE TOO HIGH?</h1>
  <p class="hero-sub">Use our free valuation tool below or book a valuation with one of our qualified surveyors.</p>
  <form class="search">
    <span class="search-hint">Enter your commercial property postcode to begin the valuation process</span>
    <span class="search-btn">START FREE VALUATION</span>
  </form>
</section>

<h2 class="features-title">A BETTER UNDERSTANDING OF YOUR RATES PAYMENT</h2>

<div class="feature" style="left:97px">
  <div class="feature-icon" style="margin-left:59px">
    <svg width="88" height="54" viewBox="0 0 88 54" fill="none" stroke="var(--orange)" stroke-width="3">
      <rect x="16" y="2" width="50" height="34" rx="2"/>
      <line x1="36" y1="36" x2="34" y2="46"/><line x1="46" y1="36" x2="48" y2="46"/>
      <line x1="28" y1="47" x2="54" y2="47" stroke-width="4"/>
      <rect x="2" y="24" width="13" height="27" rx="2" fill="var(--white)"/>
      <rect x="62" y="14" width="24" height="37" rx="2" fill="var(--white)"/>
      <line x1="15" y1="42" x2="30" y2="42"/>
    </svg>
  </div>
  <p class="feature-text">Lorem ipsum dolor sit amet, consectetur adipiscing elit. Maecenas suscipit, ipsum et lobortis aliquam, lectus dolor convallis urna, sed sodales nisi libero in nisi. Aenean euismod ex magna, fermentum finibus felis tristique non.</p>
</div>

<div class="feature" style="left:440px">
  <div class="feature-icon" style="margin-left:77px">
    <svg width="60" height="60" viewBox="0 0 60 60" fill="none" stroke="var(--orange)" stroke-width="3" stroke-linecap="round">
      <path d="M44 28V6a3 3 0 0 0-3-3H6a3 3 0 0 0-3 3v48a3 3 0 0 0 3 3h28"/>
      <line x1="11" y1="13" x2="36" y2="13"/><line x1="11" y1="21" x2="36" y2="21"/>
      <line x1="11" y1="29" x2="36" y2="29"/><line x1="11" y1="37" x2="28" y2="37"/>
      <path d="M54 30l4 4-18 18-7 2 2-7z" fill="var(--orange)"/>
    </svg>
  </div>
  <p class="feature-text">Lorem ipsum dolor sit amet, consectetur adipiscing elit. Maecenas suscipit, ipsum et lobortis aliquam, lectus dolor convallis urna, sed sodales nisi libero in nisi. Aenean euismod ex magna, fermentum finibus felis tristique non.</p>
</div>

<div class="feature" style="left:793px">
  <div class="feature-icon" style="margin-left:81px">
    <svg width="58" height="58" viewBox="0 0 58 58" fill="none" stroke="var(--orange)" stroke-width="3">
      <rect x="3" y="7" width="52" height="48" rx="3"/>
      <line x1="3" y1="17" x2="55" y2="17" stroke-width="5"/>
      <line x1="15" y1="2" x2="15" y2="11"/><line x1="43" y1="2" x2="43" y2="11"/>
      <g fill="var(--orange)" stroke="none">
        <rect x="11" y="24" width="5" height="5"/><rect x="21" y="24" width="5" height="5"/><rect x="31" y="24" width="5" height="5"/><rect x="41" y="24" width="5" height="5"/>
        <rect x="11" y="33" width="5" height="5"/><rect x="21" y="33" width="5" height="5"/><rect x="31" y="33" width="5" height="5"/><rect x="41" y="33" width="5" height="5"/>
        <rect x="11" y="42" width="5" height="5"/><rect x="21" y="42" width="5" height="5"/><rect x="31" y="42" width="5" height="5"/>
      </g>
    </svg>
  </div>
  <p class="feature-text">Lorem ipsum dolor sit amet, consectetur adipiscing elit. Maecenas suscipit, ipsum et lobortis aliquam, lectus dolor convallis urna, sed sodales nisi libero in nisi. Aenean euismod ex magna, fermentum finibus felis tristique non.</p>
</div>

<section class="covered" role="img" aria-label="Night-time illustration of a city skyline with office towers under a starry purple sky">
  <h2 class="covered-title">We’ve got you covered!</h2>
  <p class="covered-text">Lorem ipsum dolor sit amet, consectetur adipiscing elit. Maecenas suscipit, ipsum et lobortis aliquam, lectus dolor convallis urna, sed sodales nisi libero in nisi</p>
</section>

<section class="fees">
  <h2 class="fees-title">Fair fixed fees and no shock commissions!</h2>
  <p class="fees-text">Lorem ipsum dolor sit amet, consectetur adipiscing elit. Maecenas suscipit, ipsum et lobortis aliquam, lectus dolor convallis urna, sed sodales nisi libero in nisi. Aenean euismod ex magna, fermentum finibus felis tristique non. Sed eu eros est. Maecenas dignissim elit orci, vel fringilla ligula volutpat sodales. Fusce pretium sit amet lectus quis lobortis. Maecenas pulvinar pretium lobortis. Nulla vitae sem lacinia, maximus urna vel, tristique risus. Donec pellentesque eros facilisis, consequat arcu nec, convallis ante.</p>
</section>

<section class="cta">
  <p class="cta-text">BOOK A RATEABLE VALUATION WITH ONE OF OUR QUALIFIED SURVEYOR</p>
  <a class="cta-btn" href="#">BOOK VALUATION NOW</a>
</section>

<footer>
  <nav class="footer-nav">
    <a class="footer-link" style="left:560px" href="#">PRICING PLANS</a>
    <a class="footer-link" style="left:731px" href="#">FAQS</a>
    <a class="footer-link" style="left:827px" href="#">CONTACT</a>
    <a class="footer-link" style="left:955px" href="#">LEGAL &amp; TERMS</a>
  </nav>
  <p class="company-info" style="top:2165px"><b>Company Registration Number:</b> 10473856</p>
  <p class="company-info" style="top:2199px"><b>Company Registered Address:</b> Harrowgate House, Quayside Row, Leeds LS9 4QT</p>
  <div class="follow">Follow us: <span class="dot-blue"></span><span class="dot-blue"></span><span class="dot-blue"></span></div>
  <p class="copyright">© 2019 All Rights Reserved</p>
</footer>

</body>
</html>
```